Verdant Loop Advisors, LLC

I am looking for a simple, clear layout with my logo prominent and embossed, on the best quality card stock available. I would like the business name and phone number included on the card as well......I dont want my name anywhere on the card and I would like my logo embossed on the card......something simple with a white back......open to designs as long as they go along with recycling symbols and green type stuff.....The address, website, cell number, fax number, and email are listed below

5374 Tillbury Fenwood Road
Larkfield, MD 20700

c. 240.555.0143 f. 240.555.0187
e. sales@verdantloopadvisors.example
w. www.verdantloopadvisors.example

Industry/Entity Type

Recycling

```html
<!DOCTYPE html>
<html lang="en">
<head>
<meta charset="utf-8">
<title>Verdant Loop Advisors, LLC — Business Card</title>
<link rel="stylesheet" href="https://fonts.googleapis.com/css2?family=Open+Sans:wght@400;700&display=swap">
<style>
  :root {
    --backdrop: #3d3d3f;
    --card: #2a2a2c;
    --card-edge: #232325;
    --foil: #b89d7c;
    --foil-soft: #a88f72;
  }
  html, body {
    margin: 0;
    padding: 0;
    width: 1200px;
    height: 736px;
    overflow: hidden;
    background: var(--backdrop);
  }
  .canvas {
    position: relative;
    width: 1200px;
    height: 736px;
    background: radial-gradient(ellipse at 50% 40%, #4a4a4c 0%, var(--backdrop) 70%);
  }
  .card {
    position: absolute;
    left: 190px;
    top: 133px;
    width: 820px;
    height: 470px;
    background: var(--card);
    border: 1px solid var(--card-edge);
    box-shadow: 0 18px 40px rgba(0,0,0,0.45);
    font-family: "Open Sans", sans-serif;
    color: var(--foil);
  }
  .brand {
    position: absolute;
    left: 70px;
    top: 78px;
    display: flex;
    align-items: center;
    gap: 26px;
  }
  .brand-mark {
    width: 78px;
    height: 78px;
    background: var(--foil);
    flex: none;
  }
  .brand-name {
    margin: 0;
    font-weight: 700;
    font-size: 44px;
    line-height: 1.1;
    letter-spacing: 1px;
    text-transform: uppercase;
    color: var(--foil);
  }
  .brand-name .line {
    display: block;
  }
  .contact {
    position: absolute;
    left: 300px;
    top: 262px;
    margin: 0;
    padding: 0;
    list-style: none;
    font-size: 17px;
    line-height: 1.25;
    color: var(--foil-soft);
  }
  .contact li {
    display: flex;
    align-items: flex-start;
    gap: 14px;
    margin-bottom: 10px;
  }
  .contact svg {
    width: 18px;
    height: 18px;
    flex: none;
    margin-top: 1px;
    fill: var(--foil-soft);
  }
</style>
</head>
<body>
<main class="canvas">
  <section class="card" aria-label="Business card front">
    <header class="brand">
      <span class="brand-mark" aria-hidden="true"></span>
      <h1 class="brand-name">
        <span class="line">Verdant Loop</span>
        <span class="line">Advisors, LLC</span>
      </h1>
    </header>

    <ul class="contact">
      <li>
        <svg viewBox="0 0 24 24" aria-hidden="true"><rect x="3" y="8" width="18" height="12" rx="2"/><rect x="7" y="3" width="10" height="6" rx="1"/></svg>
        <span>f. 240.555.0187</span>
      </li>
      <li>
        <svg viewBox="0 0 24 24" aria-hidden="true"><path d="M6.6 10.8a15.1 15.1 0 0 0 6.6 6.6l2.2-2.2c.3-.3.7-.4 1-.2 1.1.4 2.3.6 3.6.6.6 0 1 .4 1 1V20c0 .6-.4 1-1 1A17 17 0 0 1 3 4c0-.6.4-1 1-1h3.5c.6 0 1 .4 1 1 0 1.3.2 2.5.6 3.6.1.3 0 .7-.2 1z"/></svg>
        <span>c. 240.555.0143</span>
      </li>
      <li>
        <svg viewBox="0 0 24 24" aria-hidden="true"><path d="M2 5h20v14H2z M4 7v.5l8 5 8-5V7l-8 5z" fill-rule="evenodd"/></svg>
        <span>sales@verdantloopadvisors.example</span>
      </li>
      <li>
        <svg viewBox="0 0 24 24" aria-hidden="true"><path d="M12 2a10 10 0 1 0 0 20 10 10 0 0 0 0-20zm0 2c.9 0 2.2 2 2.7 5H9.3C9.8 6 11.1 4 12 4zM4.3 11h3c0 .7 0 1.4.1 2h-3a8 8 0 0 1-.1-2zm.6 4h2.8c.3 1.5.8 2.8 1.4 3.7A8 8 0 0 1 4.9 15zm2.8-6H4.9a8 8 0 0 1 4.2-3.7c-.6.9-1.100 2.2-1.4 3.7zM12 20c-.9 0-2.2-2-2.7-5h5.4c-.5 3-1.8 5-2.7 5zm-2.9-7a18 18 0 0 1 0-2h5.8a18 18 0 0 1 0 2zm5.8 5.7c.6-.9 1.1-2.2 1.4-3.7h2.8a8 8 0 0 1-4.2 3.7zM16.6 13c.1-.6.1-1.3.1-2h3a8 8 0 0 1 0 2zm-.3-4c-.3-1.5-.8-2.8-1.4-3.7A8 8 0 0 1 19.1 9z"/></svg>
        <span>www.verdantloopadvisors.example</span>
      </li>
      <li>
        <svg viewBox="0 0 24 24" aria-hidden="true"><path d="M12 2a7 7 0 0 0-7 7c0 5.2 7 13 7 13s7-7.8 7-13a7 7 0 0 0-7-7zm0 9.5A2.5 2.5 0 1 1 12 6.5a2.5 2.5 0 0 1 0 5z"/></svg>
        <span>5374 Tillbury Fenwood Road<br>Larkfield, MD 20700</span>
      </li>
    </ul>
  </section>
</main>
</body>
</html>
```